Zielgruppe
Steuerberatung
Aufgabenstellung
Ich benötige eine Neuerstellung für ein vorhandenes Briefpapier. Bedeutet, eigentlich soll der aktuelle Inhalt neu erstellt werden, da mir die Rohdaten nicht mehr zur Verfügung stehen. Das aktuelle Briefpapier steht als .doc zur Verfügung. Ziel 1:1 Abbildung. Zudem muss die Adresse geändert werden.

```html
<!DOCTYPE html>
<html lang="de">
<head>
<meta charset="utf-8">
<title>Briefpapier Lukas Hartwig</title>
<link href="https://fonts.googleapis.com/css2?family=Roboto+Condensed:wght@400;700&display=swap" rel="stylesheet">
<style>
  :root {
    --backdrop: #808080;
    --paper: #ffffff;
    --ink: #111111;
    --mark: #4a4a4a;
    --watermark: #ebebeb;
    --rule: #555555;
  }
  html, body {
    margin: 0;
    width: 1200px;
    height: 1200px;
    overflow: hidden;
    background: var(--backdrop);
  }
  .sheet {
    position: absolute;
    left: 240px;
    top: 91px;
    width: 720px;
    height: 1018px;
    background: var(--paper);
    overflow: hidden;
    font-family: "Roboto Condensed", "Arial Narrow", sans-serif;
    color: var(--ink);
  }
  .sheet-watermark {
    position: absolute;
    left: -220px;
    top: 560px;
    width: 700px;
    height: 700px;
  }
  .brand {
    position: absolute;
    left: 523px;
    top: 92px;
    display: flex;
    align-items: center;
    gap: 8px;
  }
  .brand-square {
    width: 14px;
    height: 14px;
    border: 1.5px solid var(--mark);
    box-sizing: border-box;
  }
  .brand-name {
    font-size: 24px;
    font-weight: 700;
    color: var(--mark);
    letter-spacing: 0.5px;
  }
  .sender-line {
    position: absolute;
    left: 69px;
    top: 151px;
    font-size: 7.6px;
    white-space: nowrap;
  }
  .contact {
    position: absolute;
    left: 523px;
    top: 150px;
    font-size: 10px;
    line-height: 14.4px;
  }
  .contact-row { display: flex; white-space: nowrap; }
  .contact-label { width: 24px; }
  .contact strong { font-weight: 700; }
  .footer {
    position: absolute;
    left: 69px;
    top: 937px;
    width: 592px;
    border-top: 1px solid var(--rule);
    padding-top: 5px;
    font-size: 9px;
    line-height: 14.2px;
    white-space: nowrap;
  }
  .footer strong { font-weight: 700; }
</style>
</head>
<body>
  <div class="sheet">
    <svg class="sheet-watermark" viewBox="0 0 700 700" aria-hidden="true">
      <circle cx="350" cy="350" r="340" fill="var(--watermark)"/>
    </svg>

    <div class="brand">
      <span class="brand-square"></span>
      <span class="brand-name">Hartwig</span>
    </div>

    <div class="sender-line">Lukas Hartwig &nbsp;|&nbsp; Lindenallee 112 &nbsp;|&nbsp; 30159 Hannover</div>

    <div class="contact">
      <div class="contact-row"><strong>Lukas Hartwig</strong>&nbsp;|&nbsp;Steuerberater</div>
      <div class="contact-row"><span class="contact-label">Tel.:</span>+49 (0) 170 - 55 20 318</div>
      <div class="contact-row"><span class="contact-label">Fax.:</span>+49 (0) 511 - 60 21 77 40</div>
      <div class="contact-row"><span class="contact-label">Mail:</span>kontakt@hartwig-steuer.de</div>
      <div class="contact-row"><span class="contact-label">Web:</span>www.hartwig-steuer.de</div>
    </div>

    <div class="footer">
      <div><strong>Lukas Hartwig</strong> | Steuerberater</div>
      <div>Lindenallee 112 &nbsp;|&nbsp; 30159 Hannover &nbsp;|&nbsp; Zuständige Aufsichtsbehörde: Steuerberaterkammer Niedersachsen -Körperschaft des öffentlichen Rechts-</div>
      <div>Zuständiges Finanzamt: Finanzamt Hannover-Mitte, Steuernummer: 25/208/31764 &nbsp;|&nbsp; Bankverbindung: DE 12 3456 7890 1234 5678 90 BIC: VBKSDE2X</div>
    </div>
  </div>
</body>
</html>
```